Exclusive Social Networking Platform for future CEOs (no coding required)

We need a creative remake design (from rough mock-ups) for our social networking platform. We are a US-based start-up company called Circle Brightmoor. Our platform allows high-caliber students and young professionals that are part of established networks to reconnect online. It also has an element of Sofahopper.com (host exchange system). In terms of the layout, it can therefore be considered a combination of:
- CareerLoop (CV style profiles)
- FriendWall (messaging, pictures, posts, etc.)
- Sofahopper

UPDATE: We have been asking a few people to try to implement a map of the world (maybe just the outlines) as a backdrop to the platform, but in such a way that it is only faintly noticeable and doesn't become distracting to the platform.

If we really like your designs we may approach you for future designs for a collection of other businesses on a freelance basis (we work out of an incubator).

CONDITIONS: We are only asking for 2 pages as examples (attached PDFs). There may be an opportunity for you to design the rest of the platform as well.
Updates

Thank you very much for your designs so far! There are some very good ones among them. 

Reason: We are still waiting on several designers to provide their edited versions, and we have not yet found the designs we are looking for.

Target Market(s)

Our users are:
1. high-potential global students and young professionals
2. that have been selected to participate in high-end conferences & networks
3. and are typically entrepreneurs, techies, or young corporates
4. they love to travel
5. they are very ambitious about their careers
6. they spend a lot of time meeting people and networking

Industry/Entity Type

It Company

Requirements
Must have
• Base colours (can contain any combination of the following—you can also exclude blue if you like):
- Dark grey (almost black)
- lighter greys
- white
- blue

In terms of the design, please base it on the functional layouts we have provided (attached files). Feel free to redesign as you wish (both in colour and structure), as long as it keeps the functionality outlined by the rough sketches.
- please redesign the icons at the top (News Feed, Events, BedSwap, Expeditions) to a very simple and attractive format

NOTE: Please provide one design for each of the 2 PDF files ('RoamHub' and 'Profile') to show us how you creatively visualise the platform ('RoamHub' is the most up-to-date version considering the icons on the top and the general layout). Please also consider the attached logo to get a feeling of our brand.
Nice to have
• We would be happy to see a creative infusion of the colourful colours of our logo (see attached file). With this, it would be important that it would be kept to a minimum (as otherwise it will be distracting), so a good place to include it may be in the icons that direct people around the site, or in other parts that are more creative—up to you!

```html
<!DOCTYPE html>
<html lang="en">
<head>
<meta charset="utf-8">
<title>Circle Brightmoor – BedSwap</title>
<link href="https://fonts.googleapis.com/css2?family=Open+Sans:ital,wght@0,400;0,600;0,700;1,600&display=swap" rel="stylesheet">
<style>
:root{
  --blue:#2bb0ec;
  --blue-dark:#1e8fd0;
  --ink:#1d1d1d;
  --grey-text:#555;
  --grey-line:#c9c9c9;
  --panel:#f3f3f3;
  --card:#e9e9e9;
  --white:#fff;
  --green:#1db954;
}
*{box-sizing:border-box;margin:0;padding:0}
html,body{width:1200px;height:938px;overflow:hidden}
body{position:relative;background:var(--white);font-family:"Open Sans",Arial,sans-serif;color:var(--ink)}
.abs{position:absolute}

/* header */
.topbar{left:0;top:0;width:1200px;height:63px;background:linear-gradient(#fff,#f0f0f0);box-shadow:0 3px 6px rgba(0,0,0,.35);z-index:2}
.brand{left:44px;top:14px;display:flex;align-items:center;gap:10px;font-size:26px;font-weight:600;letter-spacing:-.3px;color:var(--ink);white-space:nowrap}
.brand-dot{width:24px;height:24px;border-radius:50%;background:var(--blue)}
.global-search{left:474px;top:14px;width:300px;height:32px;border-radius:16px;background:#e2e2e2;border:1px solid #cfcfcf;font-size:14px;padding:6px 0 0 46px;color:#333;white-space:nowrap}
.top-icons{left:900px;top:8px;display:flex;gap:22px}

/* nav */
.nav-item{top:82px;width:120px;text-align:center;font-size:18px;font-weight:700;white-space:nowrap}
.nav-item svg{display:block;margin:0 auto 6px;height:52px}
.nav-active{left:668px;top:64px;width:148px;height:148px;border-radius:50%;background:var(--blue)}

/* stage */
.stage{left:240px;top:180px;width:738px;height:758px;background:var(--panel)}
.map-thumb{left:242px;top:172px;width:124px;height:96px;background:linear-gradient(135deg,#bcd4e6,#d9e6c8 60%,#c9d9e8);border:1px solid #9ab}
.map-label{left:266px;top:254px;font-size:10px;font-weight:700;letter-spacing:1px}
.place-input{left:384px;top:202px;width:362px;height:34px;background:#dcdcdc;border:1px solid #999;font-size:24px;font-weight:700;letter-spacing:3px;padding:1px 0 0 12px;white-space:nowrap}
.place-btn{left:746px;top:202px;width:160px;height:34px;background:var(--blue);border:1px solid #777;color:#fff;font-size:18px;letter-spacing:2px;text-align:center;line-height:32px}
.trip-note{left:388px;top:242px;font-size:12px;color:#777}
.date{top:244px;font-size:13px;display:flex;align-items:center;gap:3px}
.date i{width:20px;height:14px;background:var(--blue);display:block}
.tabs{left:490px;top:271px;display:flex;border:1px solid #888}
.tab{width:103px;height:29px;text-align:center;font-size:20px;letter-spacing:2px;line-height:28px;background:#ddd}
.tab.on{background:var(--blue)}

/* side boxes */
.box{background:#fff;border:1px solid var(--grey-line);border-radius:4px;box-shadow:0 1px 3px rgba(0,0,0,.15)}
.box h3{color:var(--blue);font-size:16px;font-weight:600}
.list{font-size:12px;line-height:16px;white-space:nowrap}
.scroll{background:#e6e6e6;width:14px}
.scroll i{display:block;background:var(--blue);height:36px;margin:2px}
.chat-list{font-size:14px;line-height:19px;list-style:none}
.chat-list li{padding-left:14px;position:relative}
.chat-list li.on::before{content:"";position:absolute;left:2px;top:7px;width:6px;height:6px;border-radius:50%;background:var(--green)}
.chat-pill{left:34px;top:352px;width:154px;height:18px;border-radius:9px;background:#e3e3e3;color:var(--blue);font-size:13px;text-align:center;line-height:18px}

/* filters */
.filters{left:244px;top:340px;width:164px;height:404px;background:#fff;border:2px solid var(--blue);border-radius:3px}
.filters h4{background:var(--blue);color:#fff;font-size:16px;font-weight:600;text-align:center;height:30px;line-height:30px}
.opt{font-size:12px;display:flex;gap:6px;padding:0 10px;margin-top:12px;align-items:flex-start;line-height:17px}
.radio{width:12px;height:12px;border:1px solid #777;border-radius:50%;flex:none;margin-top:3px}
.radio.on{background:radial-gradient(var(--blue) 35%,#fff 40%)}
.stepper{display:inline-block;width:12px;height:12px;border-radius:50%;background:var(--blue);color:#fff;font-size:10px;line-height:11px;text-align:center;font-weight:700;vertical-align:middle}
.select{margin:0 20px 6px;height:22px;border:1px solid #888;background:#eee;font-size:14px;padding-left:6px;line-height:20px;display:flex;justify-content:space-between;padding-right:8px;color:#222}
.check{font-size:12px;font-weight:600;padding-left:38px;display:flex;gap:6px;align-items:center}
.check i{width:11px;height:11px;border:1px solid #555;display:block;font-style:normal;font-size:9px;line-height:9px;text-align:center}

/* profile cards */
.card{left:416px;width:540px;height:134px;background:var(--card);border-radius:4px}
.card .photo{position:absolute;left:29px;top:10px;width:84px;height:114px;background:linear-gradient(#c9b39b,#8e7763)}
.card .info{position:absolute;left:128px;top:6px;white-space:nowrap}
.card .name{color:var(--blue);font-size:22px;font-weight:600;line-height:28px}
.card .role{font-size:13.5px;font-weight:700;line-height:18px}
.card .meta{font-size:9px;font-weight:600;line-height:13px}
.card .meta b{font-weight:700}
.main-scroll{left:964px;top:342px;width:14px;height:38px;background:var(--blue)}

/* events */
.events{left:990px;top:234px;width:192px;height:462px}
.events h3{font-style:italic;text-align:center;margin-top:8px;font-weight:600}
.event{padding-left:13px;margin-top:14px;font-size:12px;line-height:16px;color:#333;white-space:nowrap}
.event strong{display:flex;gap:14px;color:var(--blue);font-size:16px;font-weight:600;line-height:22px}

/* chat dock */
.dock{top:914px;height:24px;background:var(--blue);color:#fff;font-size:16px;text-align:center;line-height:24px}
.dock .dot{display:inline-block;width:7px;height:7px;border-radius:50%;background:var(--green);margin-right:8px;vertical-align:middle}
</style>
</head>
<body>

<header class="abs topbar">
  <div class="abs brand"><span class="brand-dot"></span>Circle Brightmoor</div>
  <div class="abs global-search">|Search for people, places or network</div>
  <div class="abs top-icons">
    <svg width="52" height="46" viewBox="0 0 52 46" aria-label="Contacts"><circle cx="18" cy="12" r="8" fill="#2bb0ec"/><path d="M4 44v-14a14 12 0 0 1 28 0v14z" fill="#2bb0ec"/><circle cx="34" cy="12" r="8" fill="#2bb0ec"/><path d="M20 44v-14a14 12 0 0 1 28 0v14z" fill="#2bb0ec"/><circle cx="26" cy="20" r="7" fill="#666"/><path d="M14 46v-8a12 10 0 0 1 24 0v8z" fill="#666"/></svg>
    <svg width="66" height="46" viewBox="0 0 66 46" aria-label="Messages"><ellipse cx="22" cy="18" rx="20" ry="12" fill="#2bb0ec"/><path d="M10 26l-4 10 14-8z" fill="#2bb0ec"/><ellipse cx="44" cy="26" rx="18" ry="11" fill="#2bb0ec" stroke="#fff" stroke-width="2"/><path d="M54 34l6 8-14-6z" fill="#2bb0ec"/></svg>
    <svg width="26" height="46" viewBox="0 0 26 46" aria-label="Profile"><circle cx="13" cy="10" r="8" fill="#2bb0ec"/><path d="M1 44v-16a12 12 0 0 1 24 0v16z" fill="#2bb0ec"/></svg>
    <svg width="46" height="46" viewBox="0 0 46 46" aria-label="Settings"><g fill="#c6c6c6"><circle cx="23" cy="23" r="15"/><rect x="19" y="2" width="8" height="42"/><rect x="2" y="19" width="42" height="8"/><rect x="19" y="2" width="8" height="42" transform="rotate(45 23 23)"/><rect x="19" y="2" width="8" height="42" transform="rotate(-45 23 23)"/></g><circle cx="23" cy="23" r="7" fill="#fff"/></svg>
  </div>
</header>

<nav>
  <div class="abs nav-active"></div>
  <div class="abs nav-item" style="left:286px">
    <svg width="64" height="52" viewBox="0 0 64 52"><rect x="4" y="8" width="56" height="38" fill="#eee" stroke="#666" stroke-width="2"/><rect x="10" y="14" width="20" height="8" fill="#555"/><g stroke="#999" stroke-width="2"><line x1="10" y1="28" x2="54" y2="28"/><line x1="10" y1="34" x2="54" y2="34"/><line x1="10" y1="40" x2="54" y2="40"/><line x1="36" y1="16" x2="54" y2="16"/><line x1="36" y1="22" x2="54" y2="22"/></g></svg>News Feed</div>
  <div class="abs nav-item" style="left:426px">
    <svg width="50" height="52" viewBox="0 0 50 52"><rect x="2" y="4" width="46" height="46" fill="#fff" stroke="#2bb0ec" stroke-width="3"/><rect x="2" y="4" width="46" height="10" fill="#2bb0ec"/><g stroke="#2bb0ec" stroke-width="1.5"><line x1="2" y1="23" x2="48" y2="23"/><line x1="2" y1="32" x2="48" y2="32"/><line x1="2" y1="41" x2="48" y2="41"/><line x1="13" y1="14" x2="13" y2="50"/><line x1="24" y1="14" x2="24" y2="50"/><line x1="35" y1="14" x2="35" y2="50"/></g></svg>Events</div>
  <div class="abs nav-item" style="left:562px">
    <svg width="52" height="52" viewBox="0 0 52 52"><circle cx="26" cy="26" r="18" fill="#f0a830"/></svg>Networks</div>
  <div class="abs nav-item" style="left:682px">
    <svg width="52" height="52" viewBox="0 0 52 52" role="img" aria-label="Globe icon"><circle cx="26" cy="26" r="24" fill="#2d7fc4"/><circle cx="26" cy="26" r="24" fill="none" stroke="#1a5e99" stroke-width="2"/></svg>BedSwap</div>
  <div class="abs nav-item" style="left:805px">
    <svg width="52" height="52" viewBox="0 0 52 52"><circle cx="26" cy="26" r="24" fill="#223" stroke="#999" stroke-width="3"/><circle cx="26" cy="26" r="18" fill="#1e6aa8"/><path d="M26 10l4 16-4 16-4-16z" fill="#e33"/></svg>Expeditions</div>
</nav>

<main>
  <div class="abs stage"></div>
  <div class="abs map-thumb" role="img" aria-label="Trip builder map of Europe"></div>
  <div class="abs map-label">Trip Builder</div>
  <div class="abs place-input">Cantenbury,UK</div>
  <div class="abs place-btn">Search</div>
  <div class="abs trip-note">Add to my next trip</div>
  <div class="abs date" style="left:620px"><i></i>14/9/2013</div>
  <div class="abs date" style="left:728px"><i></i>17/13/2013</div>
  <div class="abs tabs"><div class="tab on">People</div><div class="tab">Wall</div></div>

  <aside class="abs filters">
    <h4>Show me</h4>
    <div class="opt" style="margin-top:18px"><span class="radio"></span><span>Hosts with space<br>for &nbsp;<span class="stepper">‹</span> 2 <span class="stepper">›</span></span></div>
    <div class="opt"><span class="radio on"></span>People to meet</div>
    <div class="opt"><span class="radio"></span>Other Travellers</div>
    <div class="opt"><span>Within &nbsp;<span class="stepper">‹</span> 50 <span class="stepper">›</span> miles of<br>Catenbury</span></div>
    <h4 style="margin-top:20px">Filter By</h4>
    <div class="select" style="margin-top:16px">Network <span style="color:var(--blue)">●</span></div>
    <div class="select">Last Login <span style="color:var(--blue)">▼</span></div>
    <div class="check" style="margin-top:12px"><i>✓</i>Men</div>
    <div class="check" style="margin-top:3px"><i>✓</i>Women</div>
  </aside>

  <section>
    <article class="abs card" style="top:340px"><div class="photo" role="img" aria-label="Member portrait"></div><div class="info"><div class="name">Mateo Lorenzo Vidal</div><div class="role">Co-Founder of Circle Brightmoor and Drive Quarters</div><div class="meta"><b>Membership :</b><br><b>Mission in Life :</b> Turning Acquaintance into friendship and saving the rain forests<br><b>Based in :</b> Canterbury , UK<br><b>Current Location :</b> Canterbury , UK</div></div></article>
    <article class="abs card" style="top:486px"><div class="photo" role="img" aria-label="Member portrait"></div><div class="info"><div class="name">Mateo Lorenzo Vidal</div><div class="role">Co-Founder of Circle Brightmoor and Drive Quarters</div><div class="meta"><b>Membership :</b><br><b>Mission in Life :</b> Turning Acquaintance into friendship and saving the rain forests<br><b>Based in :</b> Canterbury , UK<br><b>Current Location :</b> Canterbury , UK</div></div></article>
    <article class="abs card" style="top:624px"><div class="photo" role="img" aria-label="Member portrait"></div><div class="info"><div class="name">Mateo Lorenzo Vidal</div><div class="role">Co-Founder of Circle Brightmoor and Drive Quarters</div><div class="meta"><b>Membership :</b><br><b>Mission in Life :</b> Turning Acquaintance into friendship and saving the rain forests<br><b>Based in :</b> Canterbury , UK<br><b>Current Location :</b> Canterbury , UK</div></div></article>
    <article class="abs card" style="top:764px"><div class="photo" role="img" aria-label="Member portrait"></div><div class="info"><div class="name">Mateo Lorenzo Vidal</div><div class="role">Co-Founder of Circle Brightmoor and Drive Quarters</div><div class="meta"><b>Membership :</b><br><b>Mission in Life :</b> Turning Acquaintance into friendship and saving the rain forests<br><b>Based in :</b> Canterbury , UK<br><b>Current Location :</b> Canterbury , UK</div></div></article>
    <article class="abs card" style="top:914px"><div class="photo" role="img" aria-label="Member portrait"></div><div class="info"><div class="name">Mateo Lorenzo Vidal</div></div></article>
    <div class="abs main-scroll"></div>
  </section>
</main>

<aside class="abs box" style="left:19px;top:216px;width:209px;height:114px">
  <h3 style="padding:5px 0 0 10px;line-height:18px">My NetWorks</h3>
  <div class="list" style="padding-left:16px">Global Commerce Forum<br>Veltora<br>UCEA<br>Andean Trade Circle....</div>
  <div class="abs scroll" style="left:185px;top:18px;height:86px"><i style="height:30px;margin-top:2px"></i></div>
</aside>

<aside class="abs box" style="left:19px;top:348px;width:209px;height:348px">
  <ul class="chat-list" style="position:absolute;left:16px;top:36px">
    <li class="on">Daniel</li><li class="on">Strom Elite</li><li class="on">Tom</li><li class="on">Mike ketoe</li><li class="on">Chui Chan</li><li class="on">Larrie cloid</li><li class="on">Ethan</li><li>Robert</li><li>Julian</li><li>Samest</li><li>Trutheee</li><li>Rahel</li><li>Abdul</li><li>Bharat</li><li>Ramya</li><li>Sunitha</li>
  </ul>
  <div class="abs scroll" style="left:185px;top:30px;height:308px"><i style="height:36px"></i></div>
</aside>
<div class="abs chat-pill">Search Chat</div>

<aside class="abs box events">
  <h3>Events &amp; Dead lines</h3>
  <div class="event"><strong><span>Today</span><span>13th Sept</span></strong>Global Commerce Forum<br>Ambassador application<br>for the 16th G9F closing</div>
  <div class="event"><strong><span>Today</span><span>13th Sept</span></strong>Global Commerce Forum<br>Ambassador application<br>for the 16th G9F closing</div>
  <div class="event"><strong><span>Today</span><span>13th Sept</span></strong>Global Commerce Forum<br>Ambassador application<br>for the 16th G9F closing</div>
  <div class="event"><strong><span>Today</span><span>13th Sept</span></strong>Global Commerce Forum<br>Ambassador application<br>for the 16th G9F closing</div>
  <div class="abs scroll" style="left:172px;top:48px;height:400px"><i style="height:36px"></i></div>
</aside>

<div class="abs dock" style="left:668px;width:144px"><span class="dot"></span>Ethan</div>
<div class="abs dock" style="left:830px;width:144px"><span class="dot"></span>Daniel</div>
<div class="abs dock" style="left:996px;width:170px">Chat (7)</div>

</body>
</html>
```